Agribusiness Insurance

I would like postcard designed to attract farmers and agribusiness owners to my insurance consulting services. My business model is being a Trusted Advisor through identifying exposures, developing strategies, implementing programs and then monitoring our designed plan. I am knowledge representative (13YRs ag insurance), Represent 15 Farm + Carriers (favorable pricing/competitive multiple options) Specialized in Confinements, Cattle Farms, and Grain Producers. No Membership Fees Necessary

Many Insurance Producers in my area are nearing retirement I am 33 and am looking to promote this..

Target Market(s)

Farmers and Agribusiness Owners

Industry/Entity Type

Agribusiness

Requirements
Must have

• Tobias Renholt
Phone: Cell 555 207 4163
Email: trenholt@plainsviewcover.example

```html
<!DOCTYPE html>
<html lang="en">
<head>
<meta charset="utf-8">
<title>Agricultural Insurance Postcard</title>
<link href="https://fonts.googleapis.com/css2?family=Didact+Gothic&family=Open+Sans:wght@700;800&family=Pinyon+Script&family=Tinos:wght@400;700&display=swap" rel="stylesheet">
<style>
:root{
  --green:#1c5e30;
  --green-dark:#134421;
  --gold:#d9a53a;
  --gold-light:#f5d98a;
  --gold-dark:#8a5a14;
  --white:#ffffff;
  --ink:#111111;
  --rule:#777777;
  --label:#444444;
}
*{margin:0;padding:0;box-sizing:border-box}
html,body{width:1200px;height:1173px;overflow:hidden;background:var(--white)}
.canvas{position:relative;width:1200px;height:1173px}
.side-label{position:absolute;left:268px;font-family:"Didact Gothic",sans-serif;font-size:25px;color:var(--label)}
.side-label.front{top:22px}
.side-label.back{top:600px}

.card-front{position:absolute;left:264px;top:55px;width:700px;height:542px;background:var(--green);border:1px solid var(--green-dark);overflow:hidden}
.headline{position:absolute;left:0;right:0;top:26px;text-align:center;font-family:"Open Sans",sans-serif;font-weight:800;font-size:39px;color:var(--white);letter-spacing:.3px}
.gold-band{position:absolute;left:0;right:0;height:6px;background:linear-gradient(90deg,var(--gold-dark),var(--gold-light),var(--gold),var(--gold-light),var(--gold-dark))}
.gold-band.top{top:84px}
.gold-band.bottom{top:391px}
.field-photo{position:absolute;left:0;right:0;top:90px;height:301px;background:linear-gradient(180deg,#9fc2d6 0%,#5d8a3a 14%,#3f7a2a 40%,#6b8f38 65%,#8a7a4a 100%)}
.questions{position:absolute;left:17px;top:102px;font-family:"Open Sans",sans-serif;font-weight:700;font-size:18px;line-height:23.5px;color:var(--white);text-shadow:0 0 3px #000,0 0 2px #000}
.portrait{position:absolute;left:23px;top:290px;width:158px;height:163px;padding:7px;background:linear-gradient(135deg,var(--gold-light),var(--gold-dark),var(--gold-light),var(--gold-dark))}
.portrait-fill{width:100%;height:100%;background:linear-gradient(180deg,#a09a94,#6a5e58 60%,#2a1a1a)}
.seal{position:absolute;left:509px;top:288px;width:164px;height:164px}
.seal-text{position:absolute;left:540px;top:337px;width:100px;text-align:center;font-family:"Open Sans",sans-serif;font-weight:700;font-size:12px;line-height:14.5px;color:var(--ink)}
.name-script{position:absolute;left:192px;top:395px;font-family:"Pinyon Script",cursive;font-size:48px;color:var(--white);white-space:nowrap}
.contact{position:absolute;left:0;right:0;text-align:center;font-family:"Tinos",serif;font-size:23px;color:var(--white)}
.contact.phone{top:456px;padding-left:4px}
.contact.email{top:488px;padding-left:0}

.card-back{position:absolute;left:264px;top:629px;width:700px;height:540px;background:var(--white);border:1px solid #555}
.sender{position:absolute;left:40px;top:36px;width:280px;text-align:center;font-family:"Tinos",serif;font-weight:700;font-size:12.5px;line-height:17px;color:var(--ink)}
.sender .name-script{position:static;display:block;font-size:36px;color:var(--ink);font-weight:400;line-height:44px;margin-bottom:4px}
.divider{position:absolute;left:352px;top:80px;width:1px;height:419px;background:var(--rule)}
.stamp-box{position:absolute;left:559px;top:43px;width:87px;height:100px;border:1px solid var(--rule)}
.address-line{position:absolute;left:385px;width:266px;height:1px;background:var(--rule)}
</style>
</head>
<body>
<div class="canvas">
  <div class="side-label front">front</div>
  <section class="card-front">
    <h1 class="headline">Expert in Agricultural Insurance</h1>
    <div class="gold-band top"></div>
    <div class="field-photo" role="img" aria-label="Photo of rows of leafy crops in a farm field with a barn and trees in the distance"></div>
    <div class="questions">
      Are you looking for:<br>
      _A new&nbsp; farm carrier?<br>
      _A knowledgeable representative?<br>
      _Lower premiums?<br>
      _More options?<br>
      _Better service?
    </div>
    <div class="gold-band bottom"></div>
    <div class="portrait"><div class="portrait-fill" role="img" aria-label="Portrait photo of the insurance agent"></div></div>
    <svg class="seal" viewBox="0 0 164 164" aria-hidden="true">
      <defs>
        <radialGradient id="sealGold" cx="40%" cy="35%" r="70%">
          <stop offset="0" stop-color="#fff0b5"/>
          <stop offset=".5" stop-color="#e0a83a"/>
          <stop offset="1" stop-color="#9a6416"/>
        </radialGradient>
      </defs>
      <circle cx="82" cy="82" r="80" fill="url(#sealGold)"/>
      <circle cx="82" cy="82" r="68" fill="none" stroke="#8a5a14" stroke-width="2"/>
      <circle cx="82" cy="82" r="60" fill="#f7d684" stroke="#b57a22" stroke-width="2"/>
    </svg>
    <div class="seal-text">Favorable<br>pricing!<br>Competitive<br>multiple<br>options!</div>
    <div class="name-script">Tobias Renholt</div>
    <div class="contact phone">Phone: Cell 555 207 4163</div>
    <div class="contact email">Email: trenholt@plainsviewcover.example</div>
  </section>

  <div class="side-label back">back</div>
  <section class="card-back">
    <div class="sender">
      <span class="name-script">Tobias Renholt</span>
      Expert in Agricultural Insurance<br>
      Phone: Cell 555 207 4163<br>
      Email: trenholt@plainsviewcover.example
    </div>
    <div class="divider"></div>
    <div class="stamp-box"></div>
    <div class="address-line" style="top:323px"></div>
    <div class="address-line" style="top:376px"></div>
    <div class="address-line" style="top:431px"></div>
  </section>
</div>
</body>
</html>
```